Refresh and update our Juice bottle label to a more vibrant and eye catching brand

We’ve had this label and included trademarked logo for the past 10 years. We do change the name of the juice ands its ingredients accordingly.
I want to up-date this round juice bottle label so it is more eye catching , trendy and clearly screams (healthy/juice/delicious/refreshing/beauty/youthful/high energy.
I have attached my trademarked logos as well as examples of a few labels. I also attached a few pictures of our juices with the current label which is a 2x4 inch front and back. I want you to see how colorful our juice is. I want the updated label to include out trademarked logo somehow but add in some color or graphics that speak to the message above in (). Open to adding color and even having a wrap around label instead of front and back=

Target Market(s)

Upscale women:men, age 20-65 40:30 ratio, health/ fitness/ body aware, anti aging/ high energy/ prevention of disease. Clientele is primarily caucasian.

Industry/Entity Type

Beverage, cold-pressed juice, wellness

Font styles to use
Sans Serif

Colors
59FF00
82FF00
B8FF75
E3FFCB
F4FFEA
EB3D1F
EC4F4E
F09395
F8D3D4
FCEDEE
E54698
E96AAD
F1A4CE
F9D9EA
FCEFF6
6B429C
8869AF
B7A5CE
E3DAEB
F3F0F8

Requirements
Must have
• My trademarked logo incorporated somehow. Bright/simple/modern/trendy style. I need to be able to change out the name of the juice and its ingredients and nutritional information. I want the label to say “100% Juice” basically this all needs to be on it: Name and Address. The name and address of your juicing business. ... Name of the Food. You should list the name of the food that is commonly used. ... What is the Amount of Juice inside of the bottle? ... % of juice declaration. ... Ingredients. ... Food Allergen (made in a facility with nuts). ... The Disclaimer. Must say “cold-pressed juice”
Nice to have
• Maybe a graphic image of a piece of fruit like a lemon with sliced cucumbers, I want vibrant colors added such as maybe use hot pink -outline or graphic on my Sip Tide Calm? since the juice is pink. Or a bright yellow on my Ran Bolt? Or a bright green on Vex Lumo. Maybe some wording like “no added sugar or preservatives”, “gluten free”
Should not have
• No health guarantees

```html
<!DOCTYPE html>
<html lang="en">
<head>
<meta charset="utf-8">
<title>Ran Bolt? Cold-Pressed Juice Label</title>
<link href="https://fonts.googleapis.com/css2?family=Anton&family=Lilita+One&family=Montserrat:wght@400;700&family=Poppins:wght@600&display=swap" rel="stylesheet">
<style>
  :root {
    --backdrop: #9bd9a0;
    --forest: #0b6a35;
    --lime: #7ccf00;
    --lime-bright: #82ff00;
    --lime-pale: #b8ff75;
    --lime-mist: #e3ffcb;
    --white: #ffffff;
  }
  * { margin: 0; padding: 0; box-sizing: border-box; }
  html, body { width: 1016px; height: 1200px; overflow: hidden; }
  body { background: var(--backdrop); position: relative; }

  .label {
    position: absolute;
    left: 58px; top: 150px;
    width: 900px; height: 900px;
  }
  .label-shapes { position: absolute; inset: 0; }

  .brand {
    position: absolute;
    left: 330px; top: 100px;
    display: flex; align-items: center; gap: 14px;
    font-family: "Poppins", sans-serif;
    font-weight: 600;
    font-size: 50px;
    color: var(--forest);
    letter-spacing: -1px;
  }
  .brand-dot {
    width: 34px; height: 34px; border-radius: 50%;
    background: var(--forest);
  }

  .juice-name {
    position: absolute;
    left: 296px; top: 222px;
    width: 520px;
    font-family: "Anton", sans-serif;
    font-size: 118px;
    line-height: 1;
    color: var(--forest);
    text-transform: uppercase;
    letter-spacing: -1px;
  }

  .shelf-life {
    position: absolute;
    left: 82px; top: 418px;
    font-family: "Lilita One", sans-serif;
    font-size: 18px;
    line-height: 1.2;
    color: var(--white);
    text-transform: uppercase;
  }
  .juice-percent {
    position: absolute;
    left: 82px; top: 458px;
    font-family: "Anton", sans-serif;
    font-size: 128px;
    line-height: 1;
    color: var(--lime-bright);
  }
  .juice-type {
    position: absolute;
    left: 96px; top: 596px;
    font-family: "Anton", sans-serif;
    font-size: 50px;
    line-height: 1.05;
    color: var(--white);
    text-transform: uppercase;
    text-align: center;
  }

  .ingredients {
    position: absolute;
    left: 420px; top: 440px;
    list-style: none;
    font-family: "Lilita One", sans-serif;
    font-size: 32px;
    line-height: 48px;
    color: var(--white);
    text-transform: uppercase;
  }
  .ingredients li { display: flex; align-items: center; gap: 22px; }
  .ingredients svg { width: 30px; height: 24px; flex: none; }

  .fine-print {
    position: absolute;
    left: 130px; top: 722px;
    width: 640px;
    font-family: "Montserrat", sans-serif;
    font-size: 12.5px;
    line-height: 1.28;
    color: var(--white);
    text-align: center;
  }
  .fine-print strong { color: var(--lime-pale); }
  .website {
    display: block;
    margin-top: 10px;
    font-weight: 700;
    font-size: 18px;
    color: var(--lime-bright);
  }
</style>
</head>
<body>
  <div class="label">
    <svg class="label-shapes" viewBox="0 0 900 900" aria-hidden="true">
      <defs>
        <clipPath id="label-circle"><circle cx="450" cy="450" r="450"/></clipPath>
      </defs>
      <g clip-path="url(#label-circle)">
        <rect width="900" height="900" fill="var(--lime)"/>
        <path d="M40 0 H900 V440 C840 520 760 520 700 470 C640 410 600 340 530 352 C470 362 440 400 380 385 C300 365 250 260 170 200 L40 120 Z" fill="var(--white)"/>
        <path d="M0 0 H330 C300 60 250 140 150 172 C80 194 30 150 0 150 Z" fill="var(--lime-pale)"/>
        <circle cx="450" cy="450" r="446" fill="none" stroke="var(--lime-pale)" stroke-width="22"/>
        <path d="M0 354 C120 330 230 350 290 420 C350 500 350 640 420 690 C480 730 560 710 640 670 C720 630 790 640 830 720 L900 800 V900 H0 Z" fill="var(--forest)"/>
      </g>
    </svg>

    <div class="brand"><span class="brand-dot"></span>Leafmill Press</div>

    <h1 class="juice-name">Ran Bolt?</h1>

    <p class="shelf-life">Best if used within<br>5 days of purchase</p>
    <p class="juice-percent">100%</p>
    <p class="juice-type">Vegetable &amp;<br>Fruit Juice</p>

    <ul class="ingredients">
      <li><svg viewBox="0 0 32 26" aria-hidden="true"><path d="M2 24 C4 8 16 2 30 2 C28 16 18 24 2 24 Z" fill="var(--white)"/></svg>Pineapple</li>
      <li><svg viewBox="0 0 32 26" aria-hidden="true"><path d="M2 24 C4 8 16 2 30 2 C28 16 18 24 2 24 Z" fill="var(--white)"/></svg>Lemon</li>
      <li><svg viewBox="0 0 32 26" aria-hidden="true"><path d="M2 24 C4 8 16 2 30 2 C28 16 18 24 2 24 Z" fill="var(--white)"/></svg>Fuji Apple</li>
      <li><svg viewBox="0 0 32 26" aria-hidden="true"><path d="M2 24 C4 8 16 2 30 2 C28 16 18 24 2 24 Z" fill="var(--white)"/></svg>Turmeric Root</li>
    </ul>

    <p class="fine-print">
      <strong>COLD-PRESSED JUICE</strong> · Perishable Keep Refrigerated Shake Well *separation is natural*<br>
      WARNING: This product has not been pasteurized and, therefore may contain<br>
      harmful bacteria that can cause serious illness in children, the elderly,<br>
      and persons with weakened immune systems.<br>
      Made in a facility that processes nuts.<br>
      Net Wt. 12oz (354mL)<br>
      418 Orchard Ln #7, Fernbrook,CA 90210
      <span class="website">leafmillpress.com</span>
    </p>
  </div>
</body>
</html>
```